Packaging Design Job - Baby Diaper Rash Cream and Wipes Packaging Concepts Needed

Hello, Our baby brand “Pellora” is launching 2 new products – a Diaper Rash Cream and Diaper Wipes – and would like some creative design concepts for our product packaging.Pellora is a pharmaceutical brand that specializes in baby products. We are a mid – premium priced brand with a focus on targeting mothers between the ages of 18 – 35 years. Our products are positioned for mass market with other competitive brands such as Malvotex, Bramolux, Harvonel, and Quilbrat, to give you a better understanding of the category. What we are looking for in our packaging is an ethical, pharmaceutical look that will appeal to mothers as a product that is safe and effective for their baby. The packaging should be clean, fresh, and consumer friendly, while still maintaining that this is a clinical product. The design concepts are a box design for the Diaper Rash Cream and a plastic packaging design for the Diaper Wipes. Attached you will find the Pellora logo and examples of Diaper Rash Cream box packaging and Diaper Wipes plastic packaging from competitors (to give you an idea of what shape of packaging we like). Please feel free to contact me should you have any questions.Thank you for your time and effort,Roxa

Target Market(s)

We are a mid – premium priced brand with a focus on targeting mothers between the ages of 18 – 35 years.

Industry/Entity Type

Baby Care

Requirements
Must have
• Packaging design concepts for a box design for the Diaper Rash Cream and a plastic packaging design for the Diaper Wipes.
Nice to have
• Diaper Rash Cream box: 8 cm width, 8 cm length, 8 cm depth
• Diaper Wipes package: 23 cm width, 10.5 cm length, 4.5 cm depth

```html
<!DOCTYPE html>
<html lang="en">
<head>
<meta charset="utf-8">
<title>Pellora Diaper Care Packaging</title>
<link rel="stylesheet" href="https://fonts.googleapis.com/css2?family=Arimo:wght@700&display=swap">
<style>
  :root {
    --canvas: #ffffff;
    --mint: #a9dccd;
    --mint-deep: #94d1c1;
    --mint-light: #f1f6f3;
    --seal: #b9e3d7;
    --ink: #1d6fa3;
    --frame: #ffffff;
  }
  html, body {
    margin: 0;
    padding: 0;
    width: 1200px;
    height: 800px;
    overflow: hidden;
    background: var(--canvas);
    font-family: "Arimo", Arial, sans-serif;
  }
  .canvas {
    position: relative;
    width: 1200px;
    height: 800px;
  }
  .wipes-pack {
    position: absolute;
    left: 40px;
    top: 250px;
    width: 745px;
    height: 385px;
    border-radius: 14px;
    background: radial-gradient(ellipse 55% 60% at 55% 50%, var(--mint-light) 0%, #d6ede5 45%, var(--mint) 100%);
    overflow: hidden;
  }
  .wipes-pack .seal {
    position: absolute;
    top: 0;
    bottom: 0;
    width: 22px;
    background: var(--seal);
  }
  .wipes-pack .seal-left { left: 0; }
  .wipes-pack .seal-right { right: 0; }
  .cream-box {
    position: absolute;
    left: 861px;
    top: 294px;
    width: 299px;
    height: 297px;
    background: radial-gradient(circle at 50% 50%, #ffffff 0%, #e3f3ee 40%, var(--mint) 80%, var(--mint-deep) 100%);
  }
  .frame-lines {
    position: absolute;
    left: 0;
    top: 0;
    width: 100%;
    height: 100%;
  }
  .brand-name {
    position: absolute;
    transform: translate(-50%, -50%);
    color: var(--ink);
    font-weight: 700;
    letter-spacing: 2px;
    white-space: nowrap;
  }
  .wipes-pack .brand-name { left: 371px; top: 104px; font-size: 24px; }
  .cream-box .brand-name { left: 148px; top: 55px; font-size: 17px; letter-spacing: 1.5px; }
  .product-title {
    position: absolute;
    left: 0;
    width: 100%;
    text-align: center;
    color: var(--ink);
    font-weight: 700;
    margin: 0;
  }
  .wipes-pack .product-title { top: 170px; font-size: 38px; letter-spacing: 1px; }
  .cream-box .product-sub { top: 141px; font-size: 21px; }
  .cream-box .product-title-main { top: 183px; font-size: 25px; }
</style>
</head>
<body>
<main class="canvas">
  <section class="wipes-pack" aria-label="Pellora Diaper Wipes pack">
    <div class="seal seal-left"></div>
    <div class="seal seal-right"></div>
    <svg class="frame-lines" viewBox="0 0 745 385" aria-hidden="true">
      <polyline points="300,117 168,117 168,248 560,248 560,117 442,117" fill="none" stroke="var(--frame)" stroke-width="2"/>
    </svg>
    <span class="brand-name">PELLORA</span>
    <h1 class="product-title">DIAPER WIPES</h1>
  </section>

  <section class="cream-box" aria-label="Pellora Diaper Rash Cream box">
    <svg class="frame-lines" viewBox="0 0 299 297" aria-hidden="true">
      <polyline points="97,56 57,56 57,291 243,291 243,56 200,56" fill="none" stroke="var(--frame)" stroke-width="2"/>
    </svg>
    <span class="brand-name">PELLORA</span>
    <p class="product-title product-sub">Diaper Rash</p>
    <h2 class="product-title product-title-main">CREAM</h2>
  </section>
</main>
</body>
</html>
```